Havenry - "Where Pest Control is Free for Life..." Please see pitch deck...

Project goal, that this is a reusable template, not a one-off card
Brand and design direction, follow the logo, use the brand palette (with a color swatch table), typography and layout guidance
The Mark Vale placeholder content as a clean field-by-field table (name, title, company, address, office, cell, fax, email, havenry.com)
Print specs, 3.5 × 2 in trim, 0.125 in bleed, 300 DPI, CMYK, crop marks
Deliverables, layered editable PSD (your primary ask) plus vector .AI/.EPS and a press-ready PDF/X-1a, with fonts packaged
What you'll provide (logo, colors, fonts)
Process and sign-off, concept first, then full file package on approval.
Populate every field with this Mark Vale placeholder data so we can see the layout fully built out. We will replace it per person.
Name Mark Vale
Title Title / Position
Company Havenry
Address 487 Orchard Lane, Suite 210, Tallahassee, FL 32308
Office (850) 555-0142
Cell (850) 555-0167
Fax (850) 555-0181
Email markvale@havenry.com
Website havenry.com

We need the working, editable source files so we can update them ourselves, plus a ready-to-print export:
1. Photoshop (.PSD) — fully layered and editable, with each contact field on its own labeled text layer. This is the primary requested format.
2. Vector source — the press-standard editable format, Adobe Illustrator (.AI) and/or .EPS, since vector is preferred for crisp text and logos at print.
3. Print-ready PDF — press-quality (PDF/X-1a), CMYK, with bleed and crop marks, both sides.
4. Packaged fonts and links — include or list all fonts used, and package any linked assets so the files open correctly on our end.

Why both PSD and vector
The PSD covers our request directly and is easy for us to edit. Vector (.AI/.EPS) is what most commercial printers actually prefer for type and logos because it stays razor-sharp at any size. Providing both keeps us flexible no matter which printer we use. Have fun and keep it modern and cool the designer of the logo did a great job, see what you can do.

```html
<!DOCTYPE html>
<html lang="en">
<head>
<meta charset="utf-8">
<title>Havenry Business Card</title>
<link rel="stylesheet" href="https://fonts.googleapis.com/css2?family=Montserrat:wght@400;500;800&family=Rubik:wght@600&display=swap">
<style>
  :root {
    --backdrop: #ece6e1;
    --card-navy: #121a33;
    --card-navy-deep: #0c1327;
    --brand-teal: #16b0c0;
    --brand-teal-muted: #1e8591;
    --text-light: #f1efec;
    --rule-teal: #1597a6;
  }
  * { margin: 0; padding: 0; box-sizing: border-box; }
  html, body { width: 1067px; height: 1200px; overflow: hidden; }
  body {
    background: var(--backdrop);
    position: relative;
    font-family: "Montserrat", Arial, sans-serif;
    color: var(--text-light);
  }
  .card {
    position: absolute;
    left: 245px;
    width: 614px;
    height: 362px;
    background: linear-gradient(180deg, var(--card-navy) 0%, var(--card-navy-deep) 100%);
    overflow: hidden;
  }
  .card--front { top: 197px; }
  .card--back { top: 661px; }
  .card__band {
    position: absolute;
    left: 0; right: 0; bottom: 0;
    height: 11px;
    background: var(--brand-teal);
  }
  .brand-name {
    position: absolute;
    font-family: "Montserrat", Arial, sans-serif;
    font-weight: 800;
    color: var(--text-light);
    letter-spacing: -0.5px;
    line-height: 1;
  }
  .card--front .brand-name { left: 41px; top: 244px; font-size: 44px; }
  .card--back .brand-name { left: 47px; top: 270px; font-size: 27px; }
  .brand-block {
    position: absolute;
    left: 358px; top: 17px;
    width: 243px; height: 312px;
    border-radius: 12px;
    background: var(--brand-teal-muted);
  }
  .person__name {
    position: absolute;
    left: 47px; top: 56px;
    font-family: "Rubik", Arial, sans-serif;
    font-weight: 600;
    font-size: 37px;
    color: var(--brand-teal);
    letter-spacing: -0.3px;
    line-height: 1;
  }
  .person__title {
    position: absolute;
    left: 47px; top: 102px;
    font-size: 15px;
    font-weight: 500;
    letter-spacing: 1px;
  }
  .contact-row {
    position: absolute;
    left: 307px;
    font-size: 12.5px;
    font-weight: 500;
    letter-spacing: 1.1px;
    line-height: 17px;
    white-space: nowrap;
  }
  .contact-row .label { display: inline-block; width: 22px; }
  .contact-icon {
    position: absolute;
    left: 264px;
    width: 20px; height: 20px;
    fill: none;
    stroke: var(--brand-teal);
    stroke-width: 1.4;
    stroke-linecap: round;
    stroke-linejoin: round;
  }
  .contact-rule {
    position: absolute;
    left: 309px; width: 229px;
    height: 1px;
    background: var(--rule-teal);
  }
</style>
</head>
<body>

  <section class="card card--front">
    <div class="brand-name">Havenry</div>
    <div class="brand-block"></div>
    <div class="card__band"></div>
  </section>

  <section class="card card--back">
    <h1 class="person__name">Mark Vale</h1>
    <p class="person__title">Title/Position</p>

    <svg class="contact-icon" style="top:63px;height:26px" viewBox="0 0 20 26"><path d="M10 24C4 16 2 12 2 9a8 8 0 0 1 16 0c0 3-2 7-8 15z"/><circle cx="10" cy="9" r="3"/></svg>
    <p class="contact-row" style="top:63px">487 Orchard Lane, Suite 210,<br>Tallahassee, FL 32308</p>
    <div class="contact-rule" style="top:112px"></div>

    <svg class="contact-icon" style="top:137px" viewBox="0 0 20 20"><rect x="3" y="2" width="9" height="16"/><rect x="12" y="7" width="5" height="11"/><path d="M6 5h1M9 5h1M6 8h1M9 8h1M6 11h1M9 11h1M6 14h1M9 14h1"/></svg>
    <p class="contact-row" style="top:140px"><span class="label">O:</span> (850) 555-0142</p>

    <svg class="contact-icon" style="top:165px" viewBox="0 0 20 20"><path d="M4 2l3 0 2 4-2 2c1 2 3 4 5 5l2-2 4 2v3c0 1-1 2-2 2C9 18 2 11 2 4c0-1 1-2 2-2z"/></svg>
    <p class="contact-row" style="top:167px"><span class="label">P:</span> (850) 555-0167</p>

    <svg class="contact-icon" style="top:193px" viewBox="0 0 20 20"><rect x="5" y="2" width="10" height="5"/><rect x="2" y="7" width="16" height="8" rx="1"/><rect x="5" y="12" width="10" height="6"/></svg>
    <p class="contact-row" style="top:194px"><span class="label">F:</span> (850) 555-0181</p>
    <div class="contact-rule" style="top:240px"></div>

    <svg class="contact-icon" style="top:265px" viewBox="0 0 20 20"><rect x="2" y="4" width="16" height="12"/><path d="M2 4l8 7 8-7M2 16l6-6M18 16l-6-6"/></svg>
    <p class="contact-row" style="top:266px">markvale@havenry.com</p>

    <svg class="contact-icon" style="top:292px" viewBox="0 0 20 20"><circle cx="10" cy="10" r="8"/><ellipse cx="10" cy="10" rx="3.5" ry="8"/><path d="M2 10h16M3.5 6h13M3.5 14h13"/></svg>
    <p class="contact-row" style="top:293px">havenry.com</p>

    <div class="brand-name">Havenry</div>
    <div class="card__band"></div>
  </section>

</body>
</html>
```